Book Cover Project

This is a printed journal front and back cover design. We like the current design, but it feels a little too flat / too simple.

NOTE: we are not looking for a total makeover, just a finishing / polishing of this cover.

Here is our other book cover: https://www.shelvorix.com/Mat-Studio-Blueprint-Calm-Days/dp/7390462815/ref=tmm_hrd_swatch_0?_encoding=UTF8&qid=&sr=
it's purple and yellow (mostly purple)
this one is yellow and we're thinking to add a purple bar at the bottom

Specs: 6 in x 9 in full bleed for print

```html
<!DOCTYPE html>
<html lang="en">
<head>
<meta charset="UTF-8">
<title>Mindful Marathon Journal — Cover</title>
<link rel="stylesheet" href="https://fonts.googleapis.com/css2?family=Montserrat:wght@600;700;800&display=swap">
<style>
  :root {
    --cover-yellow: #FFD21C;
    --accent-purple: #5C5AA2;
    --ink-black: #111111;
    --wood-light: #E9CFA4;
    --wood-mid: #D2AE7C;
    --wood-shadow: #B58E5E;
  }
  html, body {
    margin: 0;
    padding: 0;
    width: 800px;
    height: 1200px;
    overflow: hidden;
    background: var(--cover-yellow);
  }
  .cover {
    position: relative;
    width: 800px;
    height: 1200px;
    background: var(--cover-yellow);
    font-family: "Montserrat", Arial, sans-serif;
    overflow: hidden;
  }
  .author-name {
    position: absolute;
    top: 26px;
    left: 0;
    width: 100%;
    margin: 0;
    text-align: center;
    font-weight: 700;
    font-size: 22px;
    letter-spacing: 2.5px;
    color: var(--accent-purple);
  }
  .book-title {
    position: absolute;
    top: 172px;
    left: 0;
    width: 100%;
    margin: 0;
    text-align: center;
    font-weight: 800;
    line-height: 1;
    text-transform: uppercase;
  }
  .book-title span {
    display: block;
    font-size: 104px;
    letter-spacing: -1px;
  }
  .title-line--dark { color: var(--ink-black); }
  .title-line--accent {
    color: var(--accent-purple);
    margin: 8px 0 6px;
  }
  .tagline {
    position: absolute;
    top: 492px;
    left: 0;
    width: 100%;
    margin: 0;
    text-align: center;
    font-weight: 600;
    font-size: 26px;
    letter-spacing: 4px;
    color: var(--accent-purple);
  }
  .tagline .dot { margin: 0 10px; }
  .runner-figure {
    position: absolute;
    left: 160px;
    top: 572px;
    width: 480px;
    height: 594px;
    border-radius: 44% 44% 30% 30% / 30% 30% 20% 20%;
    background: radial-gradient(ellipse at 48% 45%, var(--wood-light) 0%, var(--wood-mid) 45%, rgba(181,142,94,0.35) 70%, rgba(255,210,28,0) 78%);
  }
  .bottom-bar {
    position: absolute;
    left: 0;
    bottom: 0;
    width: 100%;
    height: 34px;
    background: var(--accent-purple);
  }
</style>
</head>
<body>
  <main class="cover">
    <p class="author-name">DORIAN VALE</p>
    <h1 class="book-title">
      <span class="title-line--dark">Mindful</span>
      <span class="title-line--accent">Marathon</span>
      <span class="title-line--dark">Journal</span>
    </h1>
    <p class="tagline">RUN<span class="dot">•</span>WRITE<span class="dot">•</span>TRANSFORM</p>
    <div class="runner-figure" role="img" aria-label="Wooden artist's mannequin posed mid-stride, running to the right"></div>
    <div class="bottom-bar"></div>
  </main>
</body>
</html>
```